Very Simple/Minimal Business Card Design Project

The company operates in the industrial maritime infrastructure sector in Brazil. You can find more information on our website www.navelquor.com.br WE NEED TO LOOK POWERFUL AND SERIOUS
I have attached a copy of the old cards. We would like something more professional / industrial / sexy that also includes the position.

The card can be double sided or not. We would like you to propose as many options.

Thank you
Updates

Many thanks, do let me know if you have any questions. I am under a lot of time pressure to try and have them printed over the next days or so.

Please could you use the following information

for the address: Rua Tapiraçu, 418 - Centro, Rio de Janeiro, 20135-070, Brasil

for the mobile: +55 21 8372 9041
for the landline: +55 21 4067 3859

and position:  Diretor Geral

Thakn you

Target Market(s)

Shipowners, bankers, industrial companies

Industry/Entity Type

Industrial

Requirements
Must have
• POWERFUL
SERIOUS
SOLID
BIG CORPORATION

```html
<!DOCTYPE html>
<html lang="pt-BR">
<head>
<meta charset="utf-8">
<title>Navelquor – Cartão de Visita</title>
<link rel="stylesheet" href="https://fonts.googleapis.com/css2?family=Open+Sans:wght@400;600;700;800&display=swap">
<style>
  :root {
    --green: #1a9a50;
    --navy: #2e3a66;
    --ink: #5b5b5b;
    --ink-strong: #555;
    --paper: #ffffff;
    --backdrop: #ecebe8;
    --grad-top: #179c52;
    --grad-bottom: #2d3b6a;
  }
  * { margin: 0; padding: 0; box-sizing: border-box; }
  html, body { width: 1200px; height: 900px; overflow: hidden; }
  body {
    background: var(--backdrop);
    font-family: "Open Sans", Arial, sans-serif;
    position: relative;
  }
  .card {
    position: absolute;
    left: 300px;
    width: 600px;
    height: 342px;
    overflow: hidden;
  }
  .card--front { top: 88px; background: var(--paper); }
  .card--back {
    top: 466px;
    background: linear-gradient(180deg, var(--grad-top) 0%, #1f6b5e 50%, var(--grad-bottom) 100%);
  }

  /* brand name block */
  .brand {
    position: absolute;
    display: flex;
    align-items: center;
    gap: 10px;
    font-weight: 800;
    letter-spacing: 0.5px;
  }
  .brand__mark { display: block; border-radius: 4px; }
  .card--front .brand { left: 32px; top: 146px; font-size: 31px; color: var(--navy); }
  .card--front .brand__mark { width: 48px; height: 48px; background: var(--green); }
  .card--back .brand { left: 54px; top: 140px; font-size: 38px; color: #fff; }
  .card--back .brand__mark { width: 58px; height: 58px; background: #fff; }

  /* front details */
  .person { position: absolute; left: 349px; top: 70px; color: var(--ink-strong); }
  .person__name { font-size: 16px; font-weight: 700; line-height: 1.2; }
  .person__role { font-size: 14px; line-height: 1.2; }

  .contact { position: absolute; left: 322px; top: 159px; color: var(--ink); font-size: 14px; line-height: 18px; }
  .contact__row { display: flex; align-items: flex-start; gap: 7px; }
  .contact__icon { width: 20px; height: 18px; flex: none; fill: var(--ink); }
  .contact__row--address { margin-bottom: 12px; }
  .contact__row--mail { margin-top: 4px; }

  .bands { position: absolute; left: 32px; top: 293px; width: 536px; height: 17px; }

  /* back details */
  .divider { position: absolute; left: 371px; top: 129px; width: 3px; height: 82px; background: #fff; }
  .website { position: absolute; left: 388px; top: 168px; color: #fff; font-size: 15px; }
</style>
</head>
<body>

<section class="card card--front">
  <div class="person">
    <p class="person__name">Rafael Montenegro</p>
    <p class="person__role">Diretor Geral</p>
  </div>

  <div class="brand"><span class="brand__mark"></span>NAVELQUOR</div>

  <div class="contact">
    <div class="contact__row contact__row--address">
      <svg class="contact__icon" viewBox="0 0 20 18"><path d="M10 1 1 9h3v8h4.5v-5h3v5H16V9h3z"/></svg>
      <span>Rua Tapiraçu, 418 - Centro,<br>Rio de Janeiro, 20135-070, Brasil</span>
    </div>
    <div class="contact__row">
      <svg class="contact__icon" viewBox="0 0 20 18"><circle cx="10" cy="9" r="7.5"/><path d="M7 5.5c.5-.5 1.2-.3 1.4.2l.6 1.4-.9.8c.5 1.1 1.3 1.9 2.3 2.4l.8-.9 1.4.6c.5.2.6.9.2 1.3-1.8 1.8-6.7-3.2-5.8-5.8z" fill="#fff"/></svg>
      <span>landline:&nbsp; +55 21 4067 3859</span>
    </div>
    <div class="contact__row">
      <svg class="contact__icon" viewBox="0 0 20 18"><path d="M6.5 1h7v16h-7zM8 3v10h4V3z"/><circle cx="10" cy="15" r=".9" fill="#fff"/></svg>
      <span>mobile:&nbsp; +55 21 8372 9041</span>
    </div>
    <div class="contact__row contact__row--mail">
      <svg class="contact__icon" viewBox="0 0 20 18"><path d="M2 3.5h16v11H2z" fill="none" stroke="#5b5b5b" stroke-width="1.4"/><path d="M2 3.5l8 6 8-6M2 14.5l6-5M18 14.5l-6-5" fill="none" stroke="#5b5b5b" stroke-width="1.2"/></svg>
      <span>geral@navelquor.com.br</span>
    </div>
  </div>

  <svg class="bands" viewBox="0 0 536 17" preserveAspectRatio="none">
    <polygon points="0,0 267,0 250,17 0,17" fill="var(--green)"/>
    <polygon points="283,0 536,0 536,17 266,17" fill="var(--navy)"/>
  </svg>
</section>

<section class="card card--back">
  <div class="brand"><span class="brand__mark"></span>NAVELQUOR</div>
  <span class="divider"></span>
  <p class="website">www.navelquor.com.br</p>

  <svg class="bands" viewBox="0 0 536 17" preserveAspectRatio="none">
    <polygon points="0,0 267,0 250,17 0,17" fill="#fff"/>
    <polygon points="283,0 536,0 536,17 266,17" fill="#fff"/>
  </svg>
</section>

</body>
</html>
```